Business card design for IT consulting company

Looking for a simple, modern, clean business card design.
Open to reworking our existing logo.

Attached is our current business cards which we do not like.
Ideally double sided with something simple on the back.
Rectangle / Horizonal only.
No rounded edges on the card.
White as the dominate color is preferred.

Target Market(s)

clients, legal, oil & gas, medical, professionals

Industry/Entity Type

IT, tech, consulting

Contact Information for Business Card

Name, Title, email, phone, cell, website

Font styles to use
Sans Serif

Requirements
Must have
• Clean design
Should not have
• loud colors or unusual fonts, etc

```html
<!DOCTYPE html>
<html lang="en">
<head>
<meta charset="utf-8">
<title>Nexora Business Card</title>
<link rel="stylesheet" href="https://fonts.googleapis.com/css2?family=Lato:wght@400;700&family=Montserrat:wght@700&display=swap">
<style>
  :root {
    --backdrop: #e4e6ea;
    --card: #ffffff;
    --card-edge: #c9ccd2;
    --accent-blue: #1a9ad6;
    --accent-yellow: #e3a512;
    --text-dark: #2a2c31;
    --text-muted: #5b5f68;
    --rule: #c4c7cd;
    --icon-red: #e8423f;
    --icon-amber: #f0a21c;
    --icon-navy: #1f5ea8;
    --icon-sky: #2a9ee0;
  }
  * { box-sizing: border-box; margin: 0; padding: 0; }
  html, body { width: 1200px; height: 952px; overflow: hidden; }
  body {
    background: var(--backdrop);
    font-family: "Lato", sans-serif;
    display: flex;
    flex-direction: column;
    align-items: center;
    justify-content: center;
    gap: 56px;
  }
  .card {
    position: relative;
    width: 700px;
    height: 400px;
    background: var(--card);
    border-radius: 0;
    overflow: hidden;
    box-shadow: 0 1px 0 var(--card-edge), 0 12px 28px rgba(0,0,0,.12);
  }
  .edge-line {
    position: absolute;
    left: 0; bottom: 34px;
    width: 58%;
    height: 2px;
    background: var(--accent-yellow);
  }
  .edge-band {
    position: absolute;
    right: 0; bottom: 30px;
    width: 42%;
    height: 10px;
    background: var(--accent-blue);
  }
  .brand {
    position: absolute;
    display: flex;
    align-items: center;
    gap: 14px;
    color: var(--text-dark);
    font-family: "Lato", sans-serif;
    font-weight: 700;
    font-size: 40px;
    letter-spacing: 1px;
  }
  .brand-square {
    width: 44px; height: 44px;
    background: var(--accent-blue);
  }
  .card-back .brand { left: 50%; top: 44%; transform: translate(-50%, -50%); }
  .card-back .edge-line { left: auto; right: 0; }
  .card-back .edge-band { right: auto; left: 0; }
  .card-front .brand { left: 70px; top: 112px; }
  .identity {
    position: absolute;
    left: 380px;
    top: 78px;
  }
  .person-name {
    font-family: "Montserrat", sans-serif;
    font-weight: 700;
    font-size: 34px;
    color: var(--accent-yellow);
    letter-spacing: 1px;
    text-transform: uppercase;
    white-space: nowrap;
  }
  .person-title {
    font-size: 20px;
    color: var(--text-muted);
    margin-top: 4px;
  }
  .divider {
    width: 70px; height: 1px;
    background: var(--rule);
    margin: 12px 0 14px;
  }
  .contact-list { list-style: none; }
  .contact-list li {
    display: flex;
    align-items: center;
    gap: 10px;
    font-size: 17px;
    color: var(--text-dark);
    margin-bottom: 9px;
    white-space: nowrap;
  }
  .icon {
    width: 22px; height: 22px;
    display: flex; align-items: center; justify-content: center;
  }
  .icon svg { width: 14px; height: 14px; }
  .icon-phone { background: var(--icon-red); }
  .icon-mobile { background: var(--icon-amber); }
  .icon-mail { background: var(--icon-navy); }
  .icon-web { background: var(--icon-sky); }
</style>
</head>
<body>
  <section class="card card-front">
    <div class="brand"><span class="brand-square"></span><span>Nexora</span></div>
    <div class="identity">
      <h1 class="person-name">Daniel Marsh</h1>
      <p class="person-title">IT Consultant</p>
      <div class="divider"></div>
      <ul class="contact-list">
        <li><span class="icon icon-phone"><svg viewBox="0 0 24 24"><path fill="#fff" d="M6.6 10.8a15 15 0 0 0 6.6 6.6l2.2-2.2a1 1 0 0 1 1-.25 11.4 11.4 0 0 0 3.6.57 1 1 0 0 1 1 1V20a1 1 0 0 1-1 1A17 17 0 0 1 3 4a1 1 0 0 1 1-1h3.5a1 1 0 0 1 1 1c0 1.25.2 2.45.57 3.6a1 1 0 0 1-.25 1z"/></svg></span>(800) 555-0142</li>
        <li><span class="icon icon-mobile"><svg viewBox="0 0 24 24"><rect x="6" y="2" width="12" height="20" rx="2" fill="none" stroke="#fff" stroke-width="2.2"/><circle cx="12" cy="18" r="1.3" fill="#fff"/></svg></span>(604) 555-0187</li>
        <li><span class="icon icon-mail"><svg viewBox="0 0 24 24"><rect x="2" y="5" width="20" height="14" rx="1.5" fill="none" stroke="#fff" stroke-width="2"/><path d="M2 6l10 7 10-7" fill="none" stroke="#fff" stroke-width="2"/></svg></span>daniel.marsh@nexora.ca</li>
        <li><span class="icon icon-web"><svg viewBox="0 0 24 24"><path fill="#fff" d="M4 3l16 7-7 2-2 7z"/></svg></span>www.nexora.ca</li>
      </ul>
    </div>
    <div class="edge-line"></div>
    <div class="edge-band"></div>
  </section>

  <section class="card card-back">
    <div class="brand"><span class="brand-square"></span><span>Nexora</span></div>
    <div class="edge-line"></div>
    <div class="edge-band"></div>
  </section>
</body>
</html>
```